Children's Educational Software - Login Screens

We need graphics for some basic login pages. The main requirements are a background image, buttons and background overlay (box for login fields and app icons). Must utilize responsive design for various resolutions and devices. The mock-up file provides an example of the direction we are wanting to go. The app page will require a version of the background that extends down using a solid colour. One idea would be to add some flowers, bees, etc. to help add some life to the bottom half. I like the idea of clouds and grass, but am open to anything.

Target Market(s)

Elementary teachers and young children

Coding

Coded - Design and coding required

Number of Pages Required

2 page

Font styles to use
Sans Serif

Requirements
Must have
• Responsive design for various resolutions and devices
Nice to have
• clouds, grass, new app icons if current icons don't fit with new design

```html
<!DOCTYPE html>
<html lang="en">
<head>
<meta charset="utf-8">
<title>BrightPath Learning – School Login</title>
<link rel="stylesheet" href="https://fonts.googleapis.com/css2?family=Poppins:wght@300;400;500&display=swap">
<style>
  :root {
    --brand-blue: #0288d1;
    --brand-blue-text: #1a8fd3;
    --ink: #1d1d1f;
    --body-ink: #1f1f1f;
    --muted: #8a8a8a;
    --line: #cfe3ef;
    --icon-ring: #b5b5b5;
    --icon-fill: #c9c9c9;
    --panel: #ffffff;
    --sky-1: #e8f4f6;
    --sky-2: #bfe3ea;
    --sky-3: #9fd3de;
    --meadow-1: #d9e7c8;
    --meadow-2: #8fbf6b;
  }
  * { box-sizing: border-box; margin: 0; padding: 0; }
  html, body { width: 1200px; height: 706px; overflow: hidden; }
  body { font-family: "Poppins", Arial, sans-serif; position: relative; background: var(--sky-1); }

  .site-header {
    position: absolute; left: 0; top: 0; width: 1200px; height: 93px;
    background: var(--brand-blue);
    display: flex; align-items: center; padding-left: 71px;
  }
  .brand { display: flex; align-items: center; gap: 12px; color: #fff; font-size: 30px; font-weight: 500; letter-spacing: -0.3px; }
  .brand-mark { width: 44px; height: 44px; background: #fff; border-radius: 6px; opacity: .95; }

  .scenery {
    position: absolute; left: 0; top: 93px; width: 1200px; height: 613px;
    background:
      radial-gradient(ellipse 260px 90px at 175px 110px, rgba(255,255,255,.95), rgba(255,255,255,0) 70%),
      radial-gradient(ellipse 220px 150px at 330px 230px, rgba(255,255,255,.85), rgba(255,255,255,0) 75%),
      radial-gradient(ellipse 120px 45px at 900px 30px, rgba(255,255,255,.95), rgba(255,255,255,0) 70%),
      linear-gradient(180deg, var(--sky-2) 0%, var(--sky-1) 35%, var(--sky-3) 62%, var(--meadow-1) 78%, var(--meadow-2) 100%);
  }

  .intro { position: absolute; left: 71px; top: 156px; width: 560px; }
  .intro-title { font-size: 28px; font-weight: 400; line-height: 40px; color: var(--ink); letter-spacing: .2px; }
  .intro-text { margin-top: 14px; font-size: 15.5px; line-height: 30.5px; color: var(--body-ink); width: 545px; }

  .login-panel {
    position: absolute; left: 719px; top: 178px; width: 397px; height: 397px;
    background: var(--panel); border-radius: 4px;
    box-shadow: 0 0 0 6px rgba(255,255,255,.45), 0 2px 10px rgba(0,0,0,.12);
  }
  .login-title { position: absolute; top: 18px; width: 100%; text-align: center; font-size: 30px; font-weight: 400; color: var(--brand-blue-text); letter-spacing: .5px; }
  .school-id {
    position: absolute; left: 23px; top: 83px; width: 351px; height: 46px;
    border: 1px solid var(--line); border-radius: 2px; padding: 0 14px;
    font-family: inherit; font-size: 15px; color: #555;
  }
  .school-id::placeholder { color: #7a7a7a; }
  .find-id { position: absolute; top: 146px; width: 100%; text-align: center; font-family: Arial, sans-serif; font-size: 15px; color: var(--brand-blue-text); text-decoration: underline; }

  .role-list { position: absolute; top: 196px; left: 0; width: 100%; list-style: none; }
  .role { position: absolute; width: 100px; text-align: center; }
  .role-admin { left: 5px; }
  .role-teacher { left: 147px; }
  .role-student { left: 287px; }
  .role svg { display: block; margin: 0 auto; }
  .role-label { display: block; margin-top: 5px; font-size: 16px; color: var(--brand-blue-text); }

  .subscribe-note { position: absolute; left: 23px; top: 320px; width: 355px; font-family: Arial, sans-serif; font-size: 12.5px; line-height: 20px; color: var(--muted); }
  .subscribe-note a { color: var(--muted); }
</style>
</head>
<body>
  <header class="site-header">
    <div class="brand"><span class="brand-mark"></span>BrightPath Learning</div>
  </header>

  <div class="scenery" role="img" aria-label="Painted sky with soft white clouds, butterflies and a meadow of grass and wildflowers along the bottom"></div>

  <section class="intro">
    <h1 class="intro-title">Dedicated Teachers &amp; BrightPath Learning...<br>Creating Brighter Futures</h1>
    <p class="intro-text">Lorem ipsum dolor sit amet, consectetuer adipiscing elit, se nonummy nibh euismod tincidunt ut laoreet dolore magna aliquam era volutpat. Ut wisi enim ad minim veniam, quis nostrud exerci tation ullamcorper suscipit lobortis nisl ut aliquip ex ea commodo consequat. Duis autem vel eum iriure dolor in hendrerit in vulputate.</p>
  </section>

  <main class="login-panel">
    <h2 class="login-title">SCHOOL LOGIN</h2>
    <input class="school-id" type="text" placeholder="School ID">
    <a class="find-id" href="#">Find My School ID</a>

    <ul class="role-list">
      <li class="role role-admin">
        <svg width="66" height="66" viewBox="0 0 66 66" aria-hidden="true">
          <circle cx="33" cy="33" r="31.5" fill="none" stroke="var(--icon-ring)" stroke-width="1.5"/>
          <circle cx="30" cy="24" r="8" fill="var(--icon-fill)"/>
          <path d="M18 48c0-9 5-14 12-14s10 3 11 6l-5 8z" fill="var(--icon-fill)"/>
          <circle cx="43" cy="43" r="4" fill="none" stroke="var(--icon-fill)" stroke-width="2.5"/>
          <path d="M40 46l-6 6m2-2l2 2" stroke="var(--icon-fill)" stroke-width="2.5" fill="none"/>
        </svg>
        <span class="role-label">Admin</span>
      </li>
      <li class="role role-teacher">
        <svg width="66" height="66" viewBox="0 0 66 66" aria-hidden="true">
          <circle cx="33" cy="33" r="31.5" fill="none" stroke="var(--icon-ring)" stroke-width="1.5"/>
          <rect x="28" y="17" width="22" height="17" fill="none" stroke="var(--icon-fill)" stroke-width="2.5"/>
          <circle cx="21" cy="24" r="4" fill="var(--icon-fill)"/>
          <rect x="17" y="30" width="8" height="20" rx="2" fill="var(--icon-fill)"/>
          <path d="M24 32l7-3" stroke="var(--icon-fill)" stroke-width="2.5"/>
        </svg>
        <span class="role-label">Teacher</span>
      </li>
      <li class="role role-student">
        <svg width="66" height="66" viewBox="0 0 66 66" aria-hidden="true">
          <circle cx="33" cy="33" r="31.5" fill="none" stroke="var(--icon-ring)" stroke-width="1.5"/>
          <circle cx="33" cy="21" r="6" fill="var(--icon-fill)"/>
          <path d="M19 32c5 0 10 1 14 4 4-3 9-4 14-4v15c-5 0-10 1-14 4-4-3-9-4-14-4z" fill="var(--icon-fill)"/>
          <path d="M33 36v15" stroke="#fff" stroke-width="1.5"/>
        </svg>
        <span class="role-label">Student</span>
      </li>
    </ul>

    <p class="subscribe-note">Not a BrightPath Learning subscriber?<br><a href="#">Visit our website to Learn more</a> and discover why BrightPath Learning is trusted by over 53,000 teachers</p>
  </main>
</body>
</html>
```